Business Card Design for new logo

Business card Design for new logo. Follow colors from logo.
The company has offices in multiple comtries
Want to have some bulltes on the countries and also on the main services

Something like
USA*Dominican Republic*LATAM

Consulting*Healthcare IT*Tranformation

Industry/Entity Type

Information Technology

Contact Information for Business Card

Address, Phones, countries, name and position

Miron castell

Founder and CEO

947 Quarry Ln
Mill haven, PA 16835

Mcastell@novelquin.com

www.novelquin.com

717-352-6081

828-444-4444

```html
<!DOCTYPE html>
<html lang="en">
<head>
<meta charset="UTF-8">
<title>Novelquin Health – Business Card</title>
<link rel="stylesheet" href="https://fonts.googleapis.com/css2?family=Roboto:wght@400;500;700&display=swap">
<style>
  :root {
    --brand-blue: #1f78c1;
    --brand-blue-dark: #1766a8;
    --brand-orange: #f5874f;
    --ink: #2b2b2b;
    --paper: #ffffff;
    --backdrop: #2b2c30;
    --rule: #4a90cf;
  }
  * { margin: 0; padding: 0; box-sizing: border-box; }
  html, body {
    width: 1200px;
    height: 900px;
    overflow: hidden;
    background: var(--backdrop);
    font-family: "Roboto", Arial, sans-serif;
  }
  .canvas { position: relative; width: 1200px; height: 900px; }

  .card {
    position: absolute;
    top: 300px;
    width: 525px;
    height: 300px;
    border-radius: 18px;
    overflow: hidden;
    background: var(--paper);
  }
  .card--contact { left: 45px; }
  .card--brand { left: 630px; }

  .card__shapes { position: absolute; inset: 0; width: 100%; height: 100%; }

  /* Contact side */
  .identity {
    position: absolute;
    left: 200px;
    top: 34px;
    text-align: left;
  }
  .wordmark {
    display: flex;
    align-items: center;
    gap: 8px;
    font-weight: 500;
    font-size: 17px;
    color: var(--brand-blue);
    margin-bottom: 14px;
  }
  .wordmark__dot {
    width: 14px; height: 14px; border-radius: 50%;
    background: var(--brand-orange);
  }
  .identity__name {
    font-weight: 700;
    font-size: 31px;
    color: var(--brand-blue);
    line-height: 1;
  }
  .identity__role {
    font-size: 19px;
    color: var(--ink);
    margin-top: 4px;
  }

  .contact {
    position: absolute;
    top: 205px;
    color: var(--paper);
    font-size: 14.5px;
    line-height: 1.3;
  }
  .contact--web { left: 28px; }
  .contact--phone { left: 200px; }
  .contact--address { left: 345px; }

  /* Brand side */
  .brand {
    position: absolute;
    left: 50px;
    right: 50px;
    top: 70px;
    border-top: 1px solid var(--rule);
    border-bottom: 1px solid var(--rule);
    padding: 18px 0 20px;
  }
  .brand__wordmark {
    display: flex;
    align-items: center;
    justify-content: center;
    gap: 14px;
    font-weight: 500;
    font-size: 46px;
    color: var(--brand-blue);
    line-height: 1;
  }
  .brand__dot {
    width: 30px; height: 30px; border-radius: 50%;
    background: var(--brand-orange);
  }
  .bullets {
    list-style: none;
    display: flex;
    justify-content: center;
    gap: 26px;
    margin-top: 16px;
    font-size: 15px;
    color: var(--brand-blue);
  }
  .bullets li { display: flex; align-items: center; gap: 6px; }
  .bullets li::before {
    content: "";
    width: 6px; height: 6px; border-radius: 50%;
    background: var(--brand-orange);
  }
  .bullets--regions { margin-top: 10px; }
</style>
</head>
<body>
<main class="canvas">

  <section class="card card--contact" aria-label="Contact side of business card">
    <svg class="card__shapes" viewBox="0 0 525 300" aria-hidden="true">
      <polygon points="0,0 95,0 165,182 0,182" fill="var(--brand-orange)"/>
      <polygon points="525,95 525,182 300,182" fill="var(--brand-blue)"/>
      <rect x="0" y="182" width="525" height="84" fill="var(--brand-blue)"/>
      <rect x="0" y="182" width="525" height="3" fill="var(--paper)"/>
      <rect x="0" y="266" width="525" height="4" fill="var(--paper)"/>
      <rect x="0" y="270" width="525" height="30" fill="var(--brand-orange)"/>

      <g class="icon icon--globe" transform="translate(60 183)">
        <circle r="15" fill="var(--paper)" stroke="var(--brand-blue)" stroke-width="2"/>
        <circle r="8" fill="none" stroke="var(--brand-orange)" stroke-width="1.6"/>
        <ellipse rx="3.5" ry="8" fill="none" stroke="var(--brand-orange)" stroke-width="1.4"/>
        <line x1="-8" y1="0" x2="8" y2="0" stroke="var(--brand-orange)" stroke-width="1.4"/>
      </g>
      <g class="icon icon--phone" transform="translate(240 183)">
        <circle r="15" fill="var(--paper)" stroke="var(--brand-blue)" stroke-width="2"/>
        <rect x="-8" y="-3" width="16" height="10" rx="2" fill="var(--brand-orange)"/>
        <path d="M-8,-3 Q0,-11 8,-3" fill="none" stroke="var(--brand-orange)" stroke-width="2.5"/>
        <circle r="2.5" cy="2" fill="var(--paper)"/>
      </g>
      <g class="icon icon--pin" transform="translate(400 183)">
        <circle r="15" fill="var(--paper)" stroke="var(--brand-blue)" stroke-width="2"/>
        <path d="M0,9 C-5,3 -7,0 -7,-3 A7,7 0 1 1 7,-3 C7,0 5,3 0,9 Z" fill="var(--brand-orange)"/>
        <circle cy="-3" r="2.6" fill="var(--paper)"/>
      </g>
    </svg>

    <div class="identity">
      <div class="wordmark"><span class="wordmark__dot"></span>Novelquin Health</div>
      <h1 class="identity__name">Miron castell</h1>
      <p class="identity__role">Founder and CEO</p>
    </div>

    <p class="contact contact--web">Mcastell@novelquin.com<br>www.novelquin.com</p>
    <p class="contact contact--phone">717-352-6081<br>828-444-4444</p>
    <p class="contact contact--address">947 Quarry Ln<br>Mill haven, PA 16835</p>
  </section>

  <section class="card card--brand" aria-label="Brand side of business card">
    <div class="brand">
      <div class="brand__wordmark"><span class="brand__dot"></span>Novelquin Health</div>
      <ul class="bullets bullets--services">
        <li>Consulting</li>
        <li>Healthcare IT</li>
        <li>Tranformation</li>
      </ul>
      <ul class="bullets bullets--regions">
        <li>USA</li>
        <li>Dominican Republic</li>
        <li>LATAM</li>
      </ul>
    </div>
  </section>

</main>
</body>
</html>
```